Medtech Advisory- Brixholm Equity Associates Website

We need a company website, programmed in Typo3.
The design should be clean, modern and simple based on the color and style of our logo.
Brixholm Equity Associates is a Swiss company which assists international medtech companies in relocating all or part of their business to Switzerland.
The site should consist of the following pages: Home, Offering, Customers, Team, Contact us (see also attached pdf file).
Target Market(s)
Medtech Start-ups
Industry/Entity Type
It Company
Coding
Coded - Design and coding required
Requirements
Must have
- Use of the logo provided
- page structure as described above
- programmed in Typo3 so that we can edit ourselves
- responsive for use with mobile devices
Nice to have
- eye catcher to attract readers interest, e.g. visuals

```html
<!DOCTYPE html>
<html lang="en">
<head>
<meta charset="utf-8">
<title>Our Team – Brixholm Equity Associates</title>
<link href="https://fonts.googleapis.com/css2?family=Mulish:wght@400;600;700;800&family=Lato:wght@400;700&display=swap" rel="stylesheet">
<style>
:root{
  --brand:#4a7bab;
  --brand-dark:#3e6a95;
  --ink:#222;
  --body:#3a3a3a;
  --rule:#dfe3e7;
  --crumb:#e4e4e4;
  --footer:#2b3641;
  --footer-line:#3d4955;
  --footer-text:#d8dde2;
  --bar:#4c7aa8;
}
*{box-sizing:border-box;margin:0;padding:0}
html,body{width:1200px;height:2394px;overflow:hidden;background:#fff}
body{font-family:"Lato",sans-serif;color:var(--body)}
.site-header{height:107px;position:relative}
.brand{position:absolute;left:100px;top:36px;display:flex;align-items:center;gap:10px;
  font-family:"Mulish",sans-serif;font-weight:700;font-size:19px;color:var(--brand)}
.brand-dot{width:24px;height:24px;border-radius:50%;background:var(--brand)}
.phone{position:absolute;right:99px;top:12px;display:flex;align-items:center;gap:12px;
  font-family:"Mulish",sans-serif;font-weight:700;font-size:21px;color:var(--ink)}
.phone-icon{width:34px;height:34px;border:2px solid var(--brand);border-radius:50%;display:flex;align-items:center;justify-content:center}
.main-nav{position:absolute;right:99px;top:62px;display:flex;align-items:center}
.main-nav a{font-family:"Mulish",sans-serif;font-weight:800;font-size:13.5px;color:var(--ink);text-decoration:none;
  padding:4px 14px;position:relative;text-transform:uppercase}
.main-nav a+a::before{content:"";position:absolute;left:0;top:8px;height:13px;width:1px;background:#ccc}
.main-nav a.active{color:var(--brand);border:1.5px solid var(--brand);padding:4px 18px;margin-left:6px}
.main-nav a.active::before,.main-nav a.active+a::before{display:none}
.main-nav a:last-child{padding-right:0}
.hero{height:300px;position:relative;
  background:linear-gradient(180deg,#9fb2c2 0%,#8c9a86 28%,#6f7f55 45%,#8a7a62 65%,#7a6a58 100%);
  display:flex;align-items:center;justify-content:center}
.hero h1{font-family:"Mulish",sans-serif;font-weight:700;font-size:33px;line-height:45px;color:#fff;text-align:center;
  text-shadow:0 2px 6px rgba(0,0,0,.45)}
.breadcrumb{height:35px;background:var(--crumb);padding-left:100px;display:flex;align-items:center;gap:16px;
  font-family:"Mulish",sans-serif;font-size:11.5px;color:#444}
.team{padding-top:78px}
.section-title{text-align:center;font-family:"Mulish",sans-serif;font-weight:800;font-size:35px;color:#111;line-height:44px}
.section-title span{color:var(--brand)}
.title-rule{width:400px;height:2px;background:#d9dde1;margin:19px auto 0;position:relative}
.title-rule::after{content:"";position:absolute;left:170px;width:60px;height:3px;top:-.5px;background:var(--brand)}
.intro{width:740px;margin:25px auto 0;text-align:center;font-size:13.5px;line-height:24px;color:#333}
.members{width:1002px;margin:26px auto 0}
.member{height:173px;border:1px solid var(--rule);display:flex;margin-bottom:27px}
.portrait{width:163px;height:160px;margin:5px 0 0 5px;flex:none;background:linear-gradient(160deg,#d8d8d8,#8e8e8e)}
.bio{border-left:1px solid var(--rule);margin-left:6px;padding:8px 12px 0 12px;flex:1}
.bio h2{font-family:"Mulish",sans-serif;font-weight:700;font-size:20px;color:var(--brand);line-height:26px}
.bio h2::after{content:"";display:block;width:37px;height:3px;background:var(--brand);margin:9px 0 11px}
.bio p{font-size:13px;line-height:22px;color:#333;letter-spacing:.05px}
.site-footer{position:absolute;top:2072px;left:0;width:1200px;height:278px;background:var(--footer);color:var(--footer-text)}
.f-col{position:absolute;top:36px}
.f-col h3{font-family:"Mulish",sans-serif;font-weight:700;font-size:21px;color:#fff;padding-bottom:10px;border-bottom:1px solid var(--footer-line)}
.f-col h3 span{color:#6f9ac4}
.links{left:100px;width:130px}
.links ul{list-style:none;margin-top:10px}
.links li{font-size:13px;line-height:25.7px;padding-left:12px;position:relative}
.links li::before{content:"";position:absolute;left:1px;top:11px;width:4px;height:4px;border-radius:50%;background:var(--footer-text)}
.contact{left:322px;width:215px}
.contact address{font-style:normal;font-size:13px;line-height:19px;margin-top:14px}
.contact .line{display:flex;align-items:center;gap:10px;font-size:13px;margin-top:13px}
.contact .line:first-of-type{margin-top:20px}
.quick{left:638px;width:257px}
.field{width:257px;height:34px;background:#fff;margin-top:9px;font-size:11px;color:#777;padding:0 10px;display:flex;align-items:center}
.field:first-of-type{margin-top:16px}
.field.msg{align-items:flex-start;padding-top:10px}
.submit{width:120px;height:32px;margin-top:13px;background:var(--bar);color:#fff;font-family:"Mulish",sans-serif;font-weight:700;font-size:16px;display:flex;align-items:center;justify-content:center}
.social{left:989px;width:112px}
.social .item{display:flex;align-items:center;gap:10px;font-size:12px;font-style:italic;margin-top:12px}
.social .item:first-of-type{margin-top:18px}
.social .dot{width:30px;height:30px;border-radius:50%;background:#2a88c8}
.copyright{position:absolute;top:2350px;left:0;width:1200px;height:44px;background:var(--bar);color:#fff;
  font-family:"Mulish",sans-serif;font-weight:700;font-size:12px;display:flex;align-items:center;justify-content:center}
</style>
</head>
<body>
<header class="site-header">
  <div class="brand"><span class="brand-dot"></span>Brixholm Equity Associates</div>
  <div class="phone">
    <span class="phone-icon"><svg width="16" height="16" viewBox="0 0 24 24"><path d="M6.6 10.8a15 15 0 006.6 6.6l2.2-2.2c.3-.3.7-.4 1-.2 1.1.4 2.3.6 3.6.6.6 0 1 .4 1 1V20c0 .6-.4 1-1 1A17 17 0 013 4c0-.6.4-1 1-1h3.5c.6 0 1 .4 1 1 0 1.2.2 2.4.6 3.6.1.3 0 .7-.2 1z" fill="#4a7bab"/></svg></span>
    +41 32 555 0147
  </div>
  <nav class="main-nav">
    <a>Home</a><a>Who We Are</a><a>What We Do</a><a>Our Services</a><a>Customers</a><a class="active">Team</a><a>Contact Us</a>
  </nav>
</header>

<section class="hero" role="img" aria-label="Panoramic photograph of a Swiss lakeside city with church spire and wooded hills">
  <h1>We Assist promising MedTech Companies Interested<br>in Relocating to Switzerland</h1>
</section>

<div class="breadcrumb"><span>HOME</span><span>»</span><span>TEAM</span></div>

<main class="team">
  <h2 class="section-title">Our <span>Team</span></h2>
  <div class="title-rule"></div>
  <p class="intro">Brixholm Equity Associates is formed by a group of individuals with many years of operational and management experience in the medtech industry, including all areas of the value chain</p>

  <div class="members">
    <article class="member">
      <div class="portrait" role="img" aria-label="Portrait photo of Aurel Menzing"></div>
      <div class="bio"><h2>Aurel Menzing</h2>
        <p>Aurel Menzing is a consultant for strategy development, marketing and sales with companies in the Medtech sector. Before he spent 10 years with a leading manufacturer of dental implants, where he became COO after holding various sales &amp; marketing management positions. He gained first professional experience in strategic management consulting. He holds a Master’s degree in International Cultural and Business Studies from the University of Weissach/Germany.</p></div>
    </article>
    <article class="member">
      <div class="portrait" role="img" aria-label="Portrait photo of Lucien Varenne"></div>
      <div class="bio"><h2>Lucien Varenne</h2>
        <p>Lucien Varenne has a 25 years of business experience in multiple international companies, in medical Device class III industry, fast moving consumer goods and pharma. She served as General Manager of Corvanta injectable business in France during 4 years responsible for the operation and technical development of a fast growing site. Previously she worked with Halden and Roe during 16 years in Canada, France and Switzerland. She is Chemical engineer, and holds an executive MBA from Canada.</p></div>
    </article>
    <article class="member">
      <div class="portrait" role="img" aria-label="Portrait photo of Selina Tobler"></div>
      <div class="bio"><h2>Selina Tobler</h2>
        <p>Selina Tobler is co-founder of a boutique consulting company with focus on the life science industry. Furthermore, she is the global business development responsible for an international medical device manufacturer in which she previously was head of the OEM business. Selina has profound experience not only in the medical devices industry, but also throughout the entire value chain, from strategic alignment, developing product ideas up to sales and distribution. She holds a Master’s degree in Economics from the University of Lindenau.</p></div>
    </article>
    <article class="member">
      <div class="portrait" role="img" aria-label="Portrait photo of Ruedi K. Hasler"></div>
      <div class="bio"><h2>Ruedi K. Hasler</h2>
        <p>Ruedi Hasler has over 25 years of business experience in the international environment as a member of the senior management team, as CFO and consultant to CEOs. He has a passion for financial leadership and a deep understanding of the value chain of an organization. He has a success record in setting up and developing organizational structures and processes, in change management (with a focus on Finance, IT and HR), and in the implementation of ERP systems. He holds a degree in Business Administration with focus on Finance &amp; Controlling, and is a certified international Accounting Trustee.</p></div>
    </article>
    <article class="member">
      <div class="portrait" role="img" aria-label="Portrait photo of Grant Ellery"></div>
      <div class="bio"><h2>Grant Ellery</h2>
        <p>Grant Ellery is a Medtech &amp; Medical Diagnostics Entrepreneur, holding a Biomedical MASc, and Registered Canadian Professional Engineer with experience in US, EU, Australia and Canadian healthcare market. He has profound Medtech specific knowledge in the fields of: finance, management, regulatory affairs, US reimbursement, clinical needs analysis, multi stakeholder sales, conceptual selling, product development, IP development, evaluation and protection, contract research, manufacturing. He currently is the Executive Chairman of Norhaven Orthometrics Inc. (Orthopaedic pre and post op diagnostics), and Brixholm Equity Associates SA.</p></div>
    </article>
    <article class="member">
      <div class="portrait" role="img" aria-label="Portrait photo of Mira-Lou Brändli"></div>
      <div class="bio"><h2>Mira-Lou Brändli</h2>
        <p>Mira-Lou Brändli has fifteen years of experience in the Life Sciences industry with management positions in product development, product management and business development at multi-nationals and start-ups. She currently works as general manager of a spine start-up and supports start-ups in the life sciences sector as a consultant. Her main interest lies in projects at the interface between medical devices, biotechnology and pharma. Mira-Lou Brändli holds a degree in biochemistry of Polytechnic Institute of Aarwil and a MBA of Meridia Business School, Madrid.</p></div>
    </article>
    <article class="member">
      <div class="portrait" role="img" aria-label="Portrait photo of Tobias Lindqvist"></div>
      <div class="bio"><h2>Tobias Lindqvist</h2>
        <p>Tobias Lindqvist is currently working as a consultant with various companies for engineering, technologies and project management in the MedTech sector. Before he spent 16 years with research institutes and leading manufacturers for orthopedic devices and technologies. After holding various management positions in R&amp;D he took the responsibility for global innovation management processes. Tobias holds a Master’s degree in Biomedical Engineering from the University of Kestrel/Germany.</p></div>
    </article>
  </div>
</main>

<footer class="site-footer">
  <div class="f-col links">
    <h3>Quick <span>Links</span></h3>
    <ul><li>Home</li><li>Who We Are</li><li>What We Do</li><li>Our Services</li><li>Customers</li><li>Team</li><li>Contact Us</li></ul>
  </div>
  <div class="f-col contact">
    <h3>Contact <span>Details</span></h3>
    <address>Brixholm Equity Associates SA<br>Rue des Tilleuls 14<br>2400 Valmont<br>Switzerland</address>
    <div class="line"><svg width="14" height="14" viewBox="0 0 24 24"><path d="M6.6 10.8a15 15 0 006.6 6.6l2.2-2.2c.3-.3.7-.4 1-.2 1.1.4 2.3.6 3.6.6.6 0 1 .4 1 1V20c0 .6-.4 1-1 1A17 17 0 013 4c0-.6.4-1 1-1h3.5c.6 0 1 .4 1 1 0 1.2.2 2.4.6 3.6.1.3 0 .7-.2 1z" fill="#6f9ac4"/></svg>+41 32 555 0147</div>
    <div class="line"><svg width="14" height="14" viewBox="0 0 24 24"><rect x="6" y="3" width="12" height="6" fill="#6f9ac4"/><rect x="2" y="9" width="20" height="9" rx="2" fill="#6f9ac4"/><rect x="6" y="14" width="12" height="7" fill="#fff" stroke="#6f9ac4" stroke-width="2"/></svg>+41 32 555 0148</div>
    <div class="line"><svg width="14" height="14" viewBox="0 0 24 24"><rect x="2" y="5" width="20" height="14" fill="#6f9ac4"/><path d="M2 5l10 8 10-8" stroke="#2b3641" stroke-width="2" fill="none"/></svg>info@brixholm-equity.ch</div>
  </div>
  <div class="f-col quick">
    <h3>Quick <span>Contact</span></h3>
    <div class="field">Name</div>
    <div class="field">Email</div>
    <div class="field msg">Message</div>
    <div class="submit">Submit</div>
  </div>
  <div class="f-col social">
    <h3>Follow <span>Us</span></h3>
    <div class="item"><span class="dot" style="background:#3b5998"></span>Chatterbox</div>
    <div class="item"><span class="dot"></span>Pinwire</div>
    <div class="item"><span class="dot" style="background:#1f7ab8"></span>Linkfolio</div>
  </div>
</footer>
<div class="copyright">Copyright © 2016 BRIXHOLM EQUITY ASSOCIATES. All Rights Reserved.</div>
</body>
</html>
```